Packaging for new retail dips "Quellmor"

* We require packaging for our new retail dip range.
* We have a small "Our Story" write up that we would like somewhere...
* We have approx. 7 different flavours - Hommous, Mediterranean Olive, Beetroot, Tzatziki etc. We would like one design where we can change the colour panel and the name of the dip.
* We are looking for a modern, clean, gourmet looking design - not the usual dip packaging you see on supermarket shelves.
* See my inspiration photo's.
* The Dieline attached is to scale.
Updates
Project Deadline Extended
Reason: Extension due to Dielines and Measurements not uploaded when we thought they were.
Target Market(s)
Will be going into retail supermarkets.
Industry/Entity Type
Retail
Font styles to use
Colors
Designer to choose colors to be used in the design.
Requirements
Must have
- * Please use our 'Quellmor' logo on the front and on the front side (if possible).
Nice to have
- * 'taste is everything' somewhere...
Should not have
- * No photo's of dips or photo's in general.

```html
<!DOCTYPE html>
<html lang="en">
<head>
<meta charset="utf-8">
<title>Quellmor Dips – Lid Labels</title>
<link href="https://fonts.googleapis.com/css2?family=Open+Sans:wght@300;400&family=Roboto:wght@500;700&display=swap" rel="stylesheet">
<style>
  :root {
    --page-bg: #ffffff;
    --label-dark: #1c1d1f;
    --label-edge: #111213;
    --label-mid: #2a2b2e;
    --brand-ink: #e6e6e6;
    --weight-ink: #d9d9d9;
    --name-cream: #f4efcf;
    --olive-panel: #4f5b22;
    --olive-tagline: #b9c44c;
    --hommous-panel: #ad3a19;
    --hommous-tagline: #ec8a4c;
  }
  * { box-sizing: border-box; margin: 0; padding: 0; }
  html, body {
    width: 1200px;
    height: 696px;
    overflow: hidden;
    background: var(--page-bg);
  }
  .canvas {
    position: relative;
    width: 1200px;
    height: 696px;
  }
  .lid-label {
    position: absolute;
    top: 124px;
    width: 441px;
    height: 439px;
    background: linear-gradient(90deg,
      var(--label-edge) 0%,
      var(--label-mid) 12%,
      var(--label-dark) 50%,
      var(--label-mid) 88%,
      var(--label-edge) 100%);
    box-shadow: 0 2px 6px rgba(0,0,0,0.25);
    overflow: hidden;
  }
  .lid-label--olive { left: 140px; }
  .lid-label--hommous { left: 640px; }

  .brand {
    position: absolute;
    top: 84px;
    left: 0;
    width: 100%;
    display: flex;
    justify-content: center;
    align-items: center;
    gap: 10px;
    font-family: "Open Sans", sans-serif;
    font-weight: 300;
    font-size: 26px;
    letter-spacing: 3px;
    color: var(--brand-ink);
  }
  .brand-dot {
    width: 10px;
    height: 10px;
    border-radius: 50%;
    background: var(--brand-ink);
  }

  .flavour-panel {
    position: absolute;
    top: 0;
    left: 0;
    width: 441px;
    height: 439px;
  }
  .tagline {
    font-family: "Roboto", sans-serif;
    font-weight: 500;
    font-size: 22px;
  }
  .lid-label--olive .panel-shape { fill: var(--olive-panel); }
  .lid-label--olive .tagline { fill: var(--olive-tagline); }
  .lid-label--hommous .panel-shape { fill: var(--hommous-panel); }
  .lid-label--hommous .tagline { fill: var(--hommous-tagline); }

  .flavour-name {
    position: absolute;
    left: 0;
    width: 100%;
    text-align: center;
    font-family: "Roboto", sans-serif;
    font-weight: 700;
    color: var(--name-cream);
    line-height: 1;
  }
  .flavour-name--line1 { top: 205px; font-size: 40px; letter-spacing: -0.5px; }
  .flavour-name--olive { top: 250px; font-size: 92px; letter-spacing: -2px; }
  .flavour-name--hommous { top: 203px; font-size: 76px; letter-spacing: -1px; }
  .flavour-note {
    position: absolute;
    top: 290px;
    left: 0;
    width: 100%;
    text-align: center;
    font-family: "Roboto", sans-serif;
    font-weight: 700;
    font-size: 25px;
    color: var(--name-cream);
  }
  .net-weight {
    position: absolute;
    top: 387px;
    left: 0;
    width: 100%;
    text-align: center;
    font-family: "Open Sans", sans-serif;
    font-weight: 400;
    font-size: 24px;
    color: var(--weight-ink);
  }
</style>
</head>
<body>
<main class="canvas">

  <section class="lid-label lid-label--olive">
    <svg class="flavour-panel" viewBox="0 0 441 439" aria-hidden="true">
      <path class="panel-shape" d="M0 196 H62 C72 160 112 150 220 150 C330 150 370 160 380 196 H441 V352 H0 Z"/>
      <path id="arc-olive" d="M118 192 Q220 158 324 192" fill="none"/>
      <text class="tagline"><textPath href="#arc-olive" startOffset="50%" text-anchor="middle">taste is everything</textPath></text>
    </svg>
    <div class="brand"><span class="brand-dot"></span>QUELLMOR</div>
    <div class="flavour-name flavour-name--line1">Mediterranean</div>
    <div class="flavour-name flavour-name--olive">Olive</div>
    <div class="net-weight">200g</div>
  </section>

  <section class="lid-label lid-label--hommous">
    <svg class="flavour-panel" viewBox="0 0 441 439" aria-hidden="true">
      <path class="panel-shape" d="M0 196 H52 C64 158 108 148 220 148 C334 148 378 158 390 196 H441 V352 H0 Z"/>
      <path id="arc-hommous" d="M118 192 Q220 158 324 192" fill="none"/>
      <text class="tagline"><textPath href="#arc-hommous" startOffset="50%" text-anchor="middle">taste is everything</textPath></text>
    </svg>
    <div class="brand"><span class="brand-dot"></span>QUELLMOR</div>
    <div class="flavour-name flavour-name--hommous">Hommous</div>
    <div class="flavour-note">Lorem ipsum dolor sit</div>
    <div class="net-weight">200g</div>
  </section>

</main>
</body>
</html>
```